Singer Renmika needs a CD cover for a new song "Keep the lantern lit"

Hi. My name is Renmika. I need a CD cover for my new song "Keep the lantern lit"

I want the cover to be drawn with logos of my name and the song title only this time, so "Renmika" and "Keep the lantern lit".

My song can be heard from my website: https://renmika.sitebrook-example.com/

Those logos need to be artistic. And probably very colorful. And the logo "Renmika" is at the center. The logo "Keep lantern lit" is around it. The background is also to be artistic and colorful.

jpg file is necessary.

I would appreciate that you would challenge this for me. Thanks.

Renmika

Target Market(s)

Music industry

Colors
fbee3e

Requirements
Must have
• The logos of my name and the song title only this time, so "Renmika" and "Keep the lantern lit". The logos need to be original design.
Should not have
• Something not original product, dawn from someone's work

```html
<!DOCTYPE html>
<html lang="en">
<head>
<meta charset="utf-8">
<title>Renmika – Keep the lantern lit</title>
<link rel="stylesheet" href="https://fonts.googleapis.com/css2?family=Poppins:wght@500&family=Oswald:wght@600&display=swap">
<style>
  :root {
    --ink-yellow: #fbee3e;
    --night: #0f0b1e;
    --violet-deep: #2a2150;
    --violet-mid: #6d5f9e;
    --lilac: #b9b0d6;
    --ash: #a69c98;
    --smoke: #d9d3e0;
  }
  html, body {
    margin: 0;
    padding: 0;
    width: 1200px;
    height: 1200px;
    overflow: hidden;
    background: var(--night);
  }
  .cover {
    position: relative;
    width: 1200px;
    height: 1200px;
    overflow: hidden;
  }
  .cover-artwork {
    position: absolute;
    inset: 0;
    background:
      radial-gradient(circle at 50% 78%, rgba(251,238,62,0.22) 0, rgba(251,238,62,0) 18%),
      radial-gradient(ellipse at 30% 35%, rgba(185,176,214,0.55) 0, rgba(185,176,214,0) 40%),
      radial-gradient(ellipse at 80% 70%, rgba(217,211,224,0.5) 0, rgba(217,211,224,0) 45%),
      radial-gradient(ellipse at 15% 75%, rgba(20,14,30,0.8) 0, rgba(20,14,30,0) 35%),
      linear-gradient(180deg, var(--violet-deep) 0%, var(--night) 14%, var(--violet-mid) 30%, var(--ash) 48%, var(--violet-deep) 62%, var(--ash) 80%, var(--smoke) 100%);
  }
  .cover-type {
    position: absolute;
    inset: 0;
  }
  .lens-ring {
    fill: url(#lensFill);
    stroke: #15101f;
    stroke-width: 6;
  }
  .title-arc {
    font-family: "Poppins", "Century Gothic", sans-serif;
    font-weight: 500;
    font-size: 118px;
    letter-spacing: 4px;
    fill: var(--ink-yellow);
  }
  .artist-name {
    font-family: "Poppins", "Century Gothic", sans-serif;
    font-weight: 500;
    font-size: 104px;
    fill: var(--ink-yellow);
  }
  .title-lower {
    font-family: "Oswald", "Arial Narrow", sans-serif;
    font-weight: 600;
    font-size: 80px;
    fill: var(--ink-yellow);
  }
</style>
</head>
<body>
<main class="cover">
  <div class="cover-artwork" role="img" aria-label="Abstract painted background in violet, black and grey brush strokes with scattered yellow sparks below the centre"></div>

  <svg class="cover-type" width="1200" height="1200" viewBox="0 0 1200 1200" xmlns="http://www.w3.org/2000/svg">
    <defs>
      <radialGradient id="lensFill" cx="50%" cy="55%" r="55%">
        <stop offset="0" stop-color="#1a1430"/>
        <stop offset="0.45" stop-color="#5a4f86"/>
        <stop offset="0.85" stop-color="#c9c2e0"/>
        <stop offset="1" stop-color="#8e85b0"/>
      </radialGradient>
      <path id="upperArc" d="M 290 700 A 336 336 0 0 1 962 700"/>
      <path id="lowerArc" d="M 430 860 Q 628 900 826 830"/>
    </defs>

    <circle class="lens-ring" cx="624" cy="672" r="256" role="img" aria-label="Round lens shape at the centre of the painting"/>

    <text class="title-arc">
      <textPath href="#upperArc" startOffset="50%" text-anchor="middle">KEEP THE</textPath>
    </text>

    <text class="artist-name" x="612" y="712" text-anchor="middle">RENMIKA</text>

    <text class="title-lower">
      <textPath href="#lowerArc" startOffset="50%" text-anchor="middle">LANTERN LIT</textPath>
    </text>
  </svg>
</main>
</body>
</html>
```